update of B2B website and conversion to single page

The current website needs to be modernized. I want what is commonly called a single page website. It is not actually a single page. See some examples here:
https://www.brivolane.example/
https://www.quenzo.example/
https://www.tarnwickhub.example/
Most or all graphics will be replaced.
Please see the attached spreadsheet for a rough draft of the home page layout. Convert the existing website at https://www.zorbilinfo.example/ to a single page website. We will provide the page content. You will provide all of the design, graphics, development, production deployment. etc. The look and feel should be corporate, polished, premium.

```html
<!DOCTYPE html>
<html lang="en">
<head>
<meta charset="utf-8">
<title>Zorbil Data — Enterprise Data Quality Made Easy</title>
<link href="https://fonts.googleapis.com/css2?family=Josefin+Sans:wght@400;600&family=Roboto:wght@300;400;500&family=Libre+Baskerville:wght@700&display=swap" rel="stylesheet">
<style>
:root{
  --orange:#fcb316;
  --orange-deep:#f4a20c;
  --orange-text:#f7a81b;
  --navy:#2e4a68;
  --steel:#4d6f92;
  --sky:#8fc3d9;
  --teal:#2f6f8f;
  --cloud:#eef1f4;
  --globe-blue:#3f79bf;
  --ink:#1d1d1d;
  --muted:#8a8a8a;
  --white:#ffffff;
  --cream:#fbf6ee;
  --grey-box:#eeeeee;
  --black:#000000;
  --line:#e3dccb;
}
*{margin:0;padding:0;box-sizing:border-box}
html,body{width:1200px;height:3358px;overflow:hidden;background:var(--white)}
body{position:relative;font-family:"Roboto",Arial,sans-serif;color:var(--ink)}
.abs{position:absolute}
/* nav */
.topline{left:171px;top:86px;width:864px;height:2px;background:var(--line)}
.brand{left:240px;top:98px;display:flex;align-items:center;gap:10px}
.brand-mark{width:22px;height:22px;background:var(--orange)}
.brand-name{font-family:"Roboto",sans-serif;font-weight:500;font-size:20px;color:var(--ink)}
.nav{left:446px;top:106px;width:512px;display:flex;justify-content:space-between;font-size:11px;letter-spacing:.5px;color:#555}
/* hero */
.hero{left:171px;top:140px;width:864px;height:428px;background:linear-gradient(180deg,var(--orange) 0%,var(--orange-deep) 100%);overflow:hidden}
.hero-glow{left:0;top:0;width:864px;height:428px;background:radial-gradient(ellipse 60% 70% at 88% 45%,rgba(255,255,255,.12),rgba(255,255,255,0) 70%)}
.hero-art{left:16px;top:48px;width:330px;height:330px;border-radius:50%;
  background:radial-gradient(circle at 50% 50%,var(--navy) 0%,var(--steel) 46%,rgba(77,111,146,.55) 58%,rgba(252,179,22,0) 70%)}
.hero-art-shine{left:96px;top:128px;width:170px;height:170px;border-radius:50%;
  background:radial-gradient(circle at 50% 50%,rgba(255,224,190,.55) 0%,rgba(255,224,190,0) 70%)}
.hero-title{left:378px;top:130px;font-family:"Josefin Sans",sans-serif;font-weight:600;font-size:27px;color:var(--white);letter-spacing:1px}
.hero-sub{left:378px;top:170px;width:440px;font-size:21px;font-weight:300;line-height:1.25;color:var(--white)}
.hero-points{left:378px;top:226px;font-size:17px;font-weight:300;line-height:1.3;color:var(--white)}
.btn{top:331px;width:170px;height:43px;border-radius:22px;background:var(--white);display:flex;align-items:center;justify-content:center;gap:10px;font-size:12px;color:var(--ink);text-decoration:none}
.hero-wave{left:0;top:378px;width:864px;height:50px}
/* sections */
.sec-title{left:171px;width:864px;text-align:center;font-family:"Josefin Sans",sans-serif;font-size:22px;font-weight:400;color:var(--ink)}
.divider{left:553px;width:94px;height:8px}
.feature-list{font-family:"Josefin Sans",sans-serif;font-size:17px;line-height:1.15;color:var(--ink)}
.feature-list li{list-style:none;margin-bottom:22px}
.art-quality{left:611px;top:741px;width:246px;height:202px;border-radius:18px;
  background:
    radial-gradient(circle at 78% 22%,rgba(47,111,143,.55) 0%,rgba(47,111,143,0) 32%),
    radial-gradient(ellipse at 55% 70%,rgba(143,195,217,.85) 0%,rgba(143,195,217,0) 60%),
    linear-gradient(160deg,#f7f8fa 0%,var(--cloud) 40%,#d7e7f0 100%)}
.art-globe{left:321px;top:1189px;width:279px;height:247px;border-radius:50%;
  background:
    radial-gradient(circle at 36% 32%,#ffffff 0%,#e3e7ec 30%,#b7bfc9 62%,#8e99a6 82%,rgba(63,121,191,.9) 100%)}
.art-globe-ring{left:305px;top:1180px;width:311px;height:265px;border-radius:50%;
  background:radial-gradient(ellipse at 50% 50%,rgba(63,121,191,0) 62%,rgba(63,121,191,.18) 70%,rgba(63,121,191,0) 76%)}
.sub-label{left:171px;top:1628px;width:864px;text-align:center;font-size:18px;font-weight:300;color:var(--muted)}
/* cards */
.card{height:108px;background:var(--white);border-radius:6px;box-shadow:0 2px 10px rgba(0,0,0,.15);display:flex;align-items:center;padding:0 16px;gap:14px}
.card-name{font-size:12px;font-weight:500;color:#333;width:96px;line-height:1.2}
.card-title{font-size:15px;color:var(--ink);line-height:1.2}
.card-link{font-size:11px;color:#666;margin-top:4px}
/* data boxes */
.panel{top:2021px;height:302px;background:var(--cream)}
.panel-title{width:100%;text-align:center;font-family:"Libre Baskerville",serif;font-weight:700;font-size:17px;color:#555;margin-top:14px}
.db-grid{display:grid;grid-template-columns:1fr 1fr;row-gap:40px;margin-top:34px;text-align:center;font-size:14px;font-weight:500;color:#444}
.files{display:flex;flex-direction:column;align-items:center;gap:18px;margin-top:24px}
/* reasons */
.reason{top:2499px;height:126px;background:var(--grey-box);text-align:center;padding-top:20px}
.reason-title{font-family:"Libre Baskerville",serif;font-weight:700;font-size:15px;color:#333;line-height:1.2}
.reason-note{font-size:10px;color:var(--orange-text);margin-top:22px;line-height:1.5}
/* footer */
.footer{left:171px;top:2824px;width:864px;height:262px;background:var(--orange)}
.contact-box{left:296px;top:2732px;width:636px;height:155px;background:var(--white);box-shadow:0 4px 14px rgba(0,0,0,.3);text-align:center;font-family:"Roboto",sans-serif;font-weight:300;color:var(--orange-text);padding-top:12px}
.contact-box .phone{font-size:50px;line-height:1.2}
.contact-box .email{font-size:50px;line-height:1.25;white-space:nowrap}
.foot-brand{left:171px;top:2962px;width:864px;display:flex;justify-content:center;align-items:center;gap:10px}
.foot-brand .brand-name{font-size:26px;color:var(--ink)}
.foot-tag{left:171px;top:3003px;width:864px;text-align:center;font-size:12px;color:var(--ink)}
.social{left:420px;top:3052px;width:366px;display:flex;justify-content:space-between;font-size:10px;letter-spacing:.5px;color:var(--white)}
.copyright{left:171px;top:3086px;width:864px;height:60px;background:var(--black);color:var(--white);font-size:11px;display:flex;align-items:center;justify-content:center}
</style>
</head>
<body>
<div class="abs topline"></div>
<header>
  <div class="abs brand"><span class="brand-mark"></span><span class="brand-name">Zorbil Data</span></div>
  <nav class="abs nav"><span>CONNECTORS</span><span>FEATURES</span><span>WHY DQPRIME</span><span>OFFERS</span><span>SERVICES</span><span>BLOG</span><span>COMPANY</span></nav>
</header>

<section class="abs hero">
  <div class="abs hero-glow"></div>
  <div class="abs hero-art" role="img" aria-label="Illustration of a handshake surrounded by business icons and documents"></div>
  <div class="abs hero-art-shine"></div>
  <h1 class="abs hero-title">ZORBIL DATA</h1>
  <p class="abs hero-sub">Enterprise Data Quality and Master Data Management Made Easy</p>
  <p class="abs hero-points">Cleanse addresses in 5 minutes<br>Match and Merge records in 10 minutes<br>Master records in 60 minutes</p>
  <a class="abs btn" style="left:378px"><svg width="12" height="12" viewBox="0 0 12 12"><path d="M6 1v9M2 6l4 4 4-4" fill="none" stroke="#333" stroke-width="1.4"/></svg>About Us</a>
  <a class="abs btn" style="left:558px"><svg width="14" height="11" viewBox="0 0 14 11"><rect x="1" y="1" width="12" height="9" fill="none" stroke="#333" stroke-width="1.3"/><path d="M1 1l6 5 6-5" fill="none" stroke="#333" stroke-width="1.3"/></svg>Contact Us</a>
  <svg class="abs hero-wave" viewBox="0 0 864 50" preserveAspectRatio="none"><path d="M0 40 Q60 20 120 36 T240 34 T360 38 T480 30 T600 38 T720 32 T864 36 V50 H0Z" fill="#fff"/></svg>
</section>

<h2 class="abs sec-title" style="top:628px">Data Quality</h2>
<svg class="abs divider" style="top:669px" viewBox="0 0 94 8"><path d="M4 4H90" stroke="#222" stroke-width="1"/><path d="M0 4l5-3v6zM94 4l-5-3v6z" fill="#222"/></svg>
<ul class="abs feature-list" style="left:369px;top:787px"><li>Global Address<br>Verification</li><li>Data<br>Cleansing/Enrichment</li><li>Match and Merge</li></ul>
<div class="abs art-quality" role="img" aria-label="Illustration of a tablet dashboard with data grid, target and magnifier"></div>

<h2 class="abs sec-title" style="top:1071px">Master Data Management</h2>
<svg class="abs divider" style="top:1112px" viewBox="0 0 94 8"><path d="M4 4H90" stroke="#222" stroke-width="1"/><path d="M0 4l5-3v6zM94 4l-5-3v6z" fill="#222"/></svg>
<div class="abs art-globe-ring"></div>
<div class="abs art-globe" role="img" aria-label="Illustration of a globe connected by network icons"></div>
<ul class="abs feature-list" style="left:714px;top:1276px"><li style="margin-bottom:26px">Integration</li><li style="margin-bottom:26px">Mastering</li><li>Governance</li></ul>

<h2 class="abs sec-title" style="top:1543px">Rich Connectors</h2>
<svg class="abs divider" style="top:1588px" viewBox="0 0 94 8"><path d="M4 4H90" stroke="#222" stroke-width="1"/><path d="M0 4l5-3v6zM94 4l-5-3v6z" fill="#222"/></svg>
<p class="abs sub-label">Applications</p>

<div class="abs card" style="left:210px;top:1693px;width:251px"><span class="card-name">Tarnwick Hub</span><div><div class="card-title">Tarnwick Hub</div><div class="card-link">Learn More</div></div></div>
<div class="abs card" style="left:484px;top:1693px;width:249px"><span class="card-name">Fieldora</span><div><div class="card-title">Fieldora</div><div class="card-link">Learn More...</div></div></div>
<div class="abs card" style="left:756px;top:1693px;width:249px"><span class="card-name" style="width:140px">Crestel</span><div><div class="card-title">Crestel</div><div class="card-link">Learn<br>More...</div></div></div>
<div class="abs card" style="left:210px;top:1828px;width:251px"><span class="card-name">Orvane</span><div><div class="card-title">Orvane<br>Business<br>Suite</div><div class="card-link">Learn More...</div></div></div>
<div class="abs card" style="left:484px;top:1828px;width:249px"><span class="card-name">Veltrix</span><div><div class="card-title">Veltrix<br>Dynamics*</div><div class="card-link">Learn More...</div></div></div>
<div class="abs card" style="left:756px;top:1828px;width:249px"><span class="card-name" style="width:140px">Korvan ERP</span><div><div class="card-title">Korvan*</div><div class="card-link">Learn<br>More...</div></div></div>

<div class="abs panel" style="left:231px;width:341px">
  <div class="panel-title">Databases</div>
  <div class="db-grid"><span>Orvane DB</span><span>Terravault</span><span>Elephas SQL</span><span>Norbit DB</span><span>Quarry Server</span><span>Dolphene SQL</span></div>
</div>
<div class="abs panel" style="left:621px;width:358px">
  <div class="panel-title">Files</div>
  <div class="files">
    <svg width="40" height="50" viewBox="0 0 40 50"><path d="M2 2h26l10 10v36H2z" fill="#111"/><path d="M21 24v9" stroke="#fff" stroke-width="4" stroke-linecap="round"/></svg>
    <svg width="40" height="50" viewBox="0 0 40 50"><path d="M2 2h26l10 10v36H2z" fill="none" stroke="#111" stroke-width="3"/><rect x="5" y="24" width="30" height="14" rx="3" fill="#111"/><text x="20" y="35" font-size="10" font-family="Roboto,sans-serif" fill="#fff" text-anchor="middle">CSV</text></svg>
    <svg width="40" height="46" viewBox="0 0 40 46"><rect x="10" y="2" width="28" height="40" fill="none" stroke="#111" stroke-width="3"/><path d="M24 12h10M24 20h10M24 28h10" stroke="#111" stroke-width="2"/><rect x="2" y="10" width="18" height="22" fill="#111"/></svg>
  </div>
</div>

<h2 class="abs sec-title" style="top:2415px">Reasons To Choose Us</h2>
<svg class="abs divider" style="top:2460px" viewBox="0 0 94 8"><path d="M4 4H90" stroke="#222" stroke-width="1"/><path d="M0 4l5-3v6zM94 4l-5-3v6z" fill="#222"/></svg>
<div class="abs reason" style="left:375px;width:124px"><div class="reason-title">Batch</div><div class="reason-note">On your schedule</div></div>
<div class="abs reason" style="left:531px;width:129px"><div class="reason-title">Streaming</div><div class="reason-note">Always in sync</div></div>
<div class="abs reason" style="left:690px;width:124px;padding-top:12px"><div class="reason-title">Real Time/<br>Interactive</div><div class="reason-note" style="margin-top:6px">Autocomplete Anything<br>Smart Search</div></div>

<h2 class="abs sec-title" style="top:2654px">Contact US</h2>
<svg class="abs divider" style="top:2703px" viewBox="0 0 94 8"><path d="M4 4H90" stroke="#222" stroke-width="1"/><path d="M0 4l5-3v6zM94 4l-5-3v6z" fill="#222"/></svg>

<footer>
  <div class="abs footer"></div>
  <div class="abs contact-box"><div class="phone">(555) 014-2871</div><div class="email">info@zorbilinfo.example</div></div>
  <div class="abs foot-brand"><span class="brand-mark" style="width:28px;height:28px;background:#fff"></span><span class="brand-name">Zorbil Data</span></div>
  <p class="abs foot-tag">Enterprise Data Quality Made Easy</p>
  <nav class="abs social"><span>FRIENDLINE</span><span>CHIRPCAST</span><span>WORKNET</span><span>CODEHARBOR</span></nav>
  <div class="abs copyright">© 2018 All Right Reserved @ ZorbilData</div>
</footer>
</body>
</html>
```